Xtreme Web Design

We require a web designer to create a new website design template for our business. A mixture of stock images, our images and graphic will be used. We would like a 'home' page that will stand out and a common base page design for all other pages in our site. We need to keep our current logo and will be looking for designs that stand out and relate directly to our industry (xtreme fast indoor go kart racing). We have also attached our current font that is used in our brochures and may or may not be used in your design.
We are currently opening another new facility and will be able to provide a lot of good quality racing, facility related and go kart images soon, but until then please obtain general images or images from our current site (www.brimblefrost.com.au) as required.
The design we need to be unique and sharp with options/ideas of various jquery plugins that we will utilize.
Project Deadline Extended
Reason: Being close to the busy xmas period, we have not been able to give fair feedback to some designs and would like to extend the deadline to allow for this. I thank you for your understanding.

```html
<!DOCTYPE html>
<html lang="en">
<head>
<meta charset="utf-8">
<title>Brimblefrost Indoor Kart Racing</title>
<link href="https://fonts.googleapis.com/css2?family=Anton&family=Lato:wght@300;400&family=Righteous&display=swap" rel="stylesheet">
<style>
:root{
  --sky:#00a0e3;
  --navy:#141a8c;
  --black:#000;
  --white:#fff;
  --ink:#3a3a3a;
  --photo-a:#6d7378;
  --photo-b:#9aa1a6;
}
*{margin:0;padding:0;box-sizing:border-box}
html,body{width:1036px;height:1200px;overflow:hidden;background:var(--white)}
body{position:relative;font-family:'Lato',sans-serif}
.hero-photo{position:absolute;left:0;top:0;width:1036px;height:570px;
  background:linear-gradient(115deg,#2c3a48 0%,var(--photo-a) 35%,#b84a3a 48%,var(--photo-b) 62%,#cfd3d6 100%)}
.topbar{position:absolute;left:57px;top:0;width:920px;height:36px;background:var(--sky)}
.social{position:absolute;left:12px;top:8px;display:flex;gap:6px}
.social span{width:21px;height:21px;background:var(--black);display:block}
.search{position:absolute;left:685px;top:7px;width:193px;height:22px;background:var(--white)}
.search-icon{position:absolute;left:885px;top:6px}
.header{position:absolute;left:57px;top:36px;width:920px;height:80px;background:var(--black)}
.brand{position:absolute;left:0;top:0;width:324px;height:80px;display:flex;align-items:center;justify-content:center;
  font-family:'Righteous',sans-serif;font-size:24px;color:var(--sky);letter-spacing:1px}
.nav{position:absolute;left:325px;top:0;height:74px;display:flex;font-family:'Righteous',sans-serif;font-size:15px;color:var(--white);text-transform:uppercase}
.nav a{color:inherit;text-decoration:none;display:flex;align-items:center;padding:0 16px;height:74px}
.nav a.active{background:var(--sky);width:100px;height:80px;padding:0 0 6px;justify-content:center}
.hero-title{position:absolute;right:71px;background:var(--black);color:var(--white);font-family:'Anton',sans-serif;font-weight:400;font-size:48px;letter-spacing:1.5px;line-height:1;white-space:nowrap;display:flex;align-items:center;justify-content:center}
.hero-title.one{left:543px;top:161px;height:66px}
.hero-title.two{left:612px;top:232px;height:65px}
.slider{position:absolute;left:387px;top:448px;width:271px;height:49px;background:var(--black)}
.slider svg{position:absolute;left:0;top:0}
.panels{position:absolute;left:57px;top:497px;width:920px;height:211px;display:flex}
.panel{position:relative;height:211px;color:var(--white)}
.panel.news{width:307px;background:linear-gradient(160deg,#2aa7e6,#1a8fd0)}
.panel.social-event{width:306px;background:linear-gradient(160deg,#5e5e5e,#3a3a3a)}
.panel.corporate{width:307px;background:linear-gradient(160deg,#4a4a4a,#262626)}
.tab{position:absolute;top:46px;height:46px;font-family:'Righteous',sans-serif;font-weight:400;font-size:19px;text-transform:uppercase;display:flex;align-items:center;padding-left:13px;white-space:nowrap}
.tab::after{content:"";position:absolute;left:18px;bottom:-10px;border-right:10px solid transparent;border-top:10px solid var(--navy)}
.panel.news .tab{left:30px;width:192px;background:var(--black)}
.panel.news .tab::after{border-top-color:var(--black)}
.panel.social-event .tab{left:33px;width:232px;background:var(--navy)}
.panel.corporate .tab{left:21px;width:229px;background:var(--navy)}
.panel p{position:absolute;top:124px;font-size:14.5px;line-height:18px;width:256px}
.panel.news p{left:29px;width:262px}
.panel.social-event p{left:25px}
.panel.corporate p{left:21px;width:275px}
.about-head{position:absolute;left:57px;top:754px}
.about-head span{position:absolute;left:11px;top:10px;font-family:'Righteous',sans-serif;font-size:20px;color:var(--white);text-transform:uppercase;white-space:nowrap}
.about-text{position:absolute;left:64px;top:821px;width:606px;font-weight:300;font-size:13.4px;line-height:16.5px;color:var(--ink)}
.about-text p{margin-bottom:16px}
.kart-image{position:absolute;left:682px;top:775px;width:295px;height:283px;background:linear-gradient(180deg,#fafafa 0%,#e4e4e4 55%,#fafafa 100%)}
.footer{position:absolute;left:0;top:1061px;width:1036px;height:139px;background:var(--black);color:var(--white)}
.footer-brand{position:absolute;left:72px;top:30px;font-family:'Righteous',sans-serif;font-size:24px;color:var(--sky);letter-spacing:1px}
.address{position:absolute;right:74px;top:27px;text-align:right;font-family:'Righteous',sans-serif;font-style:normal;font-size:14px;line-height:16.3px;letter-spacing:1px;text-transform:uppercase}
.copyright{position:absolute;left:59px;top:106px;font-size:12.5px;white-space:nowrap}
.legal{position:absolute;right:70px;top:106px;font-size:12.5px;white-space:nowrap}
</style>
</head>
<body>
<div class="hero-photo" role="img" aria-label="Racing driver in helmet and race suit driving a kart with number 124 on track"></div>

<div class="topbar">
  <div class="social"><span></span><span></span></div>
  <div class="search"></div>
  <svg class="search-icon" width="24" height="24" viewBox="0 0 24 24"><circle cx="14" cy="9" r="6.5" fill="none" stroke="#fff" stroke-width="2.2"/><line x1="9.5" y1="13.5" x2="3" y2="20" stroke="#fff" stroke-width="2.6"/></svg>
</div>

<header class="header">
  <div class="brand">BRIMBLEFROST</div>
  <nav class="nav">
    <a class="active" href="#">Pricing</a>
    <a href="#">Specials</a>
    <a href="#">Group Events</a>
    <a href="#">Locations</a>
    <a href="#">About Us</a>
  </nav>
</header>

<h1 class="hero-title one">Adrenalin Fuelled</h1>
<div class="hero-title two">Racing Action</div>

<div class="slider">
  <svg width="271" height="49" viewBox="0 0 271 49">
    <polyline points="26,13 14,24.5 26,36" fill="none" stroke="#fff" stroke-width="1.6"/>
    <polyline points="43,13 55,24.5 43,36" fill="none" stroke="#fff" stroke-width="1.6"/>
    <circle cx="94" cy="25" r="19" fill="#555" stroke="#00a0e3" stroke-width="3"/>
    <circle cx="143" cy="25" r="19" fill="#8a2b24" stroke="#fff" stroke-width="3"/>
    <circle cx="190" cy="25" r="19" fill="#7a3a30" stroke="#fff" stroke-width="3"/>
    <circle cx="242" cy="25" r="19" fill="#3c3c3c" stroke="#fff" stroke-width="3"/>
  </svg>
</div>

<section class="panels">
  <article class="panel news" role="img" aria-label="Blue tinted kart racing photo">
    <h2 class="tab">Latest News</h2>
    <p>Kelsey Cove is now open with the latest in karting technology direct from Europe.</p>
  </article>
  <article class="panel social-event" role="img" aria-label="Greyscale photo of a workplace group at the track">
    <h2 class="tab">Workplace Social</h2>
    <p>Make it a battle of the sexes or a battle between departments. Qualify, grid up and take to the track at speeds up to 70 kph millimetres from the track.</p>
  </article>
  <article class="panel corporate" role="img" aria-label="Greyscale photo of drivers racing karts">
    <h2 class="tab">Corporate Events</h2>
    <p>A event with adrenalin is guaranteed to impress your guests. From promotional launches to family gatherings, a corporate event will deliver lasting memories.</p>
  </article>
</section>

<div class="about-head">
  <svg width="187" height="44" viewBox="0 0 187 44">
    <polygon points="0,0 168,0 146,44 0,44" fill="#141a8c"/>
    <polygon points="172,0 180,0 158,44 150,44" fill="#141a8c"/>
    <polygon points="184,0 187,0 187,2 166,44 158,44 180,0" fill="#141a8c"/>
  </svg>
  <span>About Us</span>
</div>

<div class="about-text">
  <p>Brimblefrost Indoor Kart Racing offers its guests a challenging, scientifically engineered racetrack. Our track is considered to be one of the finest indoor tracks in Australia.</p>
  <p>Our track has been designed by professional racers to challenge our customers - whether it's your first time in a kart or you've been racing for years, Brimblefrost Indoor Kart Racing has it all.</p>
  <p>Our high powered custom built go karts are capable of speeds over 70kph.&nbsp; No other karting centre can offer the exhilarating experience that Brimblefrost Indoor Kart Racing does.</p>
  <p>Brimblefrost Indoor Kart Racing's dedication to the safety of our drivers is always our number one concern. Passing areas and the carefully engineered barrier system ensure a safe racing environment.</p>
</div>

<div class="kart-image" role="img" aria-label="Red, black and white racing kart number 1"></div>

<footer class="footer">
  <div class="footer-brand">BRIMBLEFROST</div>
  <address class="address">24 Marlow<br>Drive Ashfield Park<br>517 Dunmore<br>Rd Kelsey Cove</address>
  <div class="copyright">Copyright (C) 2013 brimblefrost.com</div>
  <div class="legal">Privacy | Terms and Conditions | Disclaimer | Copyright Notice | Cookies Policy | Linking Policy</div>
</footer>
</body>
</html>
```